R.T. Halvorsen Electric Holiday Party Invitation

We need a cohesive, on-brand holiday party invitation suite for R.T. Halvorsen Electrical Contractors (slogan Powered Past Limits). Design should include: 1) 5x7" invitation (print + digital), 2) matching RSVP card, and 3) raffle ticket.
Use our brand colors (navy, red, white, light gray) and modern professional style with subtle holiday accents.
Event: Thursday, Dec 18 2025 | 6-10 PM | Brambleton Hall, 418 Larkspur Ave, Hammonton NJ 08094.
RSVP by: Dec 1 | Plus one allowed.
Deliver print-ready PDFs + editable source files.

```html
<!DOCTYPE html>
<html lang="en">
<head>
<meta charset="utf-8">
<title>R.T. Halvorsen Electric Holiday Party Suite</title>
<link rel="stylesheet" href="https://fonts.googleapis.com/css2?family=Gloock&family=Lexend:wght@400;500;600;700&family=Archivo+Black&display=swap">
<style>
  :root{
    --bg:#a3c2ea;
    --navy:#1b2a5e;
    --plum:#4a2458;
    --red:#e11d2a;
    --wine:#8c2437;
    --gray:#4d4d4f;
    --soft:#e9ebf1;
    --white:#ffffff;
    --display:"Gloock", Georgia, serif;
    --body:"Lexend", Arial, sans-serif;
    --heavy:"Archivo Black", Arial, sans-serif;
  }
  *{box-sizing:border-box;margin:0;padding:0}
  html,body{width:1200px;height:905px;overflow:hidden;background:var(--bg);font-family:var(--body)}
  .board{position:relative;width:1200px;height:905px}
  .shadow{box-shadow:0 18px 30px rgba(40,70,130,.35)}

  /* RSVP card */
  .rsvp{position:absolute;left:81px;top:91px;width:496px;height:495px;background:var(--white)}
  .rsvp__flakes{position:absolute;left:0;top:90px;width:150px;height:360px;
    background:radial-gradient(ellipse at 40% 50%,rgba(214,170,190,.35),rgba(255,255,255,0) 70%)}
  .rsvp__letters{position:absolute;left:58px;top:66px;display:flex;flex-direction:column;gap:2px;
    font-family:var(--heavy);color:var(--navy);font-size:96px;line-height:90px;text-align:center;width:90px}
  .brand{font-family:var(--body);font-weight:700;color:var(--navy);line-height:1.15;text-align:center}
  .rsvp__brand{position:absolute;left:166px;top:96px;width:150px;font-size:12px}
  .rsvp__title{position:absolute;left:163px;top:176px;font-family:var(--display);color:var(--navy);font-size:42px;letter-spacing:-.5px}
  .rsvp__deadline{position:absolute;left:164px;top:246px;font-size:12px;font-weight:600;color:var(--red)}
  .rsvp__name{position:absolute;left:164px;top:287px;font-size:12px;color:var(--gray);display:flex;align-items:flex-end;gap:14px}
  .rsvp__name span.line{display:block;width:176px;border-bottom:1px solid var(--gray);margin-bottom:2px}
  .rsvp__choices{position:absolute;left:164px;top:328px;display:flex;gap:18px;font-size:11.5px;color:var(--gray);line-height:1.2}
  .choice{display:flex;align-items:center;gap:15px}
  .choice i{display:block;width:22px;height:22px;border:1.3px solid var(--navy)}
  .rsvp__plus{position:absolute;left:164px;top:382px;font-size:12px;font-weight:700;color:var(--navy)}

  /* Ticket */
  .ticket{position:absolute;left:107px;top:623px;width:324px;height:176px;color:var(--white);
    background:linear-gradient(160deg,#1c2a60 0%,#23295e 45%,#5b2656 100%);
    border-radius:0 8px 8px 0;
    clip-path:polygon(10px 0,100% 0,100% 100%,10px 100%,0 165px,10px 154px,0 143px,10px 132px,0 121px,10px 110px,0 99px,10px 88px,0 77px,10px 66px,0 55px,10px 44px,0 33px,10px 22px,0 11px)}
  .ticket__title{position:absolute;left:33px;top:26px;font-family:var(--display);font-size:39px;letter-spacing:-.5px}
  .ticket__cols{position:absolute;left:33px;top:92px;display:flex}
  .tcol{padding-right:8px;margin-right:8px;border-right:1px solid rgba(255,255,255,.8);font-size:12px;line-height:1.05}
  .tcol:last-child{border:0}
  .tcol svg{display:block;margin-bottom:6px}
  .tcol .big{font-size:19px;font-weight:600}
  .tcol .red{color:var(--red)}
  .tcol.venue{font-size:9.5px;line-height:1.15}
  .stub{position:absolute;left:432px;top:623px;width:119px;height:176px;background:var(--white);
    border-radius:8px 0 0 8px;text-align:center;
    clip-path:polygon(0 0,calc(100% - 10px) 0,100% 11px,calc(100% - 10px) 22px,100% 33px,calc(100% - 10px) 44px,100% 55px,calc(100% - 10px) 66px,100% 77px,calc(100% - 10px) 88px,100% 99px,calc(100% - 10px) 110px,100% 121px,calc(100% - 10px) 132px,100% 143px,calc(100% - 10px) 154px,100% 165px,calc(100% - 10px) 100%,0 100%)}
  .stub__brand{margin:54px auto 0;width:90px;font-size:8px}
  .stub__name{margin-top:16px;font-size:13px;font-weight:700;color:var(--navy)}
  .stub__phone{font-size:8.5px;font-weight:600;color:var(--navy);display:flex;justify-content:center;align-items:center;gap:2px}

  /* Invitation */
  .invite{position:absolute;left:614px;top:91px;width:505px;height:708px;background:var(--white);overflow:hidden}
  .invite__ornaments{position:absolute;left:309px;top:0;width:196px;height:100%;
    background:linear-gradient(180deg,rgba(225,29,42,.10) 0%,rgba(140,36,55,.10) 45%,rgba(200,205,215,.18) 100%)}
  .invite__brand{position:absolute;left:43px;top:70px;width:214px;font-size:20px}
  .invite__title{position:absolute;left:43px;top:200px;font-family:var(--display);font-size:80px;line-height:80px;letter-spacing:-1px;
    background:linear-gradient(90deg,var(--wine) 0%,var(--plum) 50%,var(--navy) 100%);-webkit-background-clip:text;background-clip:text;color:transparent}
  .invite__when{position:absolute;left:43px;top:405px;display:flex}
  .when__date{padding-right:12px;border-right:1.5px solid var(--navy)}
  .when__day{font-size:33px;font-weight:600;color:var(--navy);line-height:38px}
  .when__year{font-size:42px;font-weight:700;color:var(--gray);line-height:44px}
  .when__time{padding-left:12px;font-size:26px;font-weight:500;color:var(--navy);line-height:25px;padding-top:2px}
  .when__time .red{color:var(--red);font-weight:600;display:block;margin-top:6px}
  .invite__where{position:absolute;left:43px;top:535px;display:flex;gap:10px}
  .where__venue{font-size:20px;font-weight:500;color:var(--red)}
  .where__addr{font-size:18px;color:var(--gray);line-height:23px;margin-top:3px}
</style>
</head>
<body>
<main class="board">

  <section class="rsvp shadow" aria-label="RSVP card">
    <div class="rsvp__flakes" role="img" aria-label="Soft scattered snowflake decoration"></div>
    <div class="rsvp__letters" aria-label="RSVP"><span>R</span><span>S</span><span>V</span><span>P</span></div>
    <div class="brand rsvp__brand">R.T. Halvorsen Electrical Contractors</div>
    <h1 class="rsvp__title">Holiday Party</h1>
    <p class="rsvp__deadline">Kindly respond by December 1</p>
    <div class="rsvp__name">Name: <span class="line"></span></div>
    <div class="rsvp__choices">
      <div class="choice"><i></i><span>Accepts<br>the invitation</span></div>
      <div class="choice"><i></i><span>Decline<br>the invitation</span></div>
    </div>
    <p class="rsvp__plus">Plus one allowed</p>
  </section>

  <section class="ticket shadow" aria-label="Raffle ticket">
    <h2 class="ticket__title">Holiday Party</h2>
    <div class="ticket__cols">
      <div class="tcol">
        <svg width="9" height="9" viewBox="0 0 10 10"><rect x="0.5" y="1.5" width="9" height="8" fill="none" stroke="#fff"/><rect x="0.5" y="1.5" width="9" height="2" fill="#fff"/></svg>
        <div class="big" style="font-size:14px">18, DEC</div><div class="big">2025</div>
      </div>
      <div class="tcol">
        <svg width="10" height="10" viewBox="0 0 10 10"><circle cx="5" cy="5" r="5" fill="#fff"/><path d="M5 2v3h2" stroke="#1c2a60" stroke-width="1.2" fill="none"/></svg>
        <div>6:00 to<br>10:00 PM</div><div class="red">Thursday</div>
      </div>
      <div class="tcol venue">
        <svg width="8" height="10" viewBox="0 0 8 10"><path d="M4 0a4 4 0 0 1 4 4c0 3-4 6-4 6S0 7 0 4a4 4 0 0 1 4-4z" fill="#fff"/><circle cx="4" cy="4" r="1.5" fill="#1c2a60"/></svg>
        <div class="red">Brambleton Hall</div>
        <div style="margin-top:8px">418 Larkspur Ave, Hammonton,<br>NJ 08094</div>
      </div>
    </div>
  </section>
  <aside class="stub shadow" aria-label="Ticket stub">
    <div class="brand stub__brand">R.T. Halvorsen Electrical Contractors</div>
    <div class="stub__name">RT Halvorsen</div>
    <div class="stub__phone"><svg width="7" height="7" viewBox="0 0 10 10"><path d="M2 0l2 2-1 2c1 1 2 2 3 3l2-1 2 2-2 2C4 10 0 6 0 2z" fill="#1b2a5e"/></svg>609-555-0142</div>
  </aside>

  <section class="invite shadow" aria-label="Invitation">
    <div class="invite__ornaments" role="img" aria-label="Hanging snowflake ornaments and flowing line decoration"></div>
    <div class="brand invite__brand">R.T. Halvorsen Electrical Contractors</div>
    <h1 class="invite__title">Holiday<br>Party</h1>
    <div class="invite__when">
      <div class="when__date"><div class="when__day">18, DEC</div><div class="when__year">2025</div></div>
      <div class="when__time">6:00 to<br>10:00 PM<span class="red">Thursday</span></div>
    </div>
    <div class="invite__where">
      <svg width="14" height="18" viewBox="0 0 8 10" style="margin-top:4px"><path d="M4 0a4 4 0 0 1 4 4c0 3-4 6-4 6S0 7 0 4a4 4 0 0 1 4-4z" fill="#1b2a5e"/><circle cx="4" cy="4" r="1.5" fill="#fff"/></svg>
      <div>
        <div class="where__venue">Brambleton Hall</div>
        <div class="where__addr">418 Larkspur Ave, Hammonton,<br>NJ 08094</div>
      </div>
    </div>
  </section>

</main>
</body>
</html>
```